Customer Special Orders Infographic and FAQ

Create a dazzling, unique infographic and FAQ for a new and improved customer special order process being rolled out by Birchpoint Supply.

The infographic should be unique, eye-catching and extremely engaging. Some important notes:

* Needs to be on 8-1/2x11" sheet of paper.
* 1st page is the infographic. 2nd page is the FAQ
* Font size needs to be size 12 or higher.
* You can use the photos I provided to help drive the points, but not necessary to use them.
* Target audience is store owners for Birchpoint Supply. Corporate would like them to use this new program .
* Content for the infographic in the Word document. This is p. 1.
* Content for the FAQ in the PDF - p. 2. IGNORE p. 1 of the PDF.
* See my notes in PDF p. 2, and account for the when creating the PDF
* Use Birchpoint Supply colors in the brochure (red and black)

Target Market(s)

Birchpoint Supply Store Owners

Industry/Entity Type

Retail

Font styles to use
Serif

Colors
EB3D1F
EC4F4E
F09395
F8D3D4
FCEDEE

Requirements
Must have
• Unique, Dazzling, and Eye-Catching!
Should not have
• Old school looking

```html
<!DOCTYPE html>
<html lang="en">
<head>
<meta charset="utf-8">
<title>In-Aisle Customer Special Orders FAQ</title>
<link href="https://fonts.googleapis.com/css2?family=Merriweather:wght@700;900&family=Source+Serif+4:wght@400;600;700&display=swap" rel="stylesheet">
<style>
  :root {
    --red: #eb3d1f;
    --red-soft: #ec4f4e;
    --pink: #f09395;
    --blush: #f8d3d4;
    --mist: #fcedee;
    --ink: #2a2422;
    --ink-soft: #4a403d;
    --backdrop: #ececea;
    --paper: #ffffff;
  }
  * { box-sizing: border-box; margin: 0; padding: 0; }
  html, body { width: 1200px; height: 800px; overflow: hidden; }
  body {
    background: var(--backdrop);
    font-family: "Source Serif 4", Georgia, serif;
    color: var(--ink);
    display: flex; align-items: center; justify-content: center;
  }
  .sheet {
    position: relative;
    width: 590px; height: 764px;
    background: linear-gradient(100deg, var(--paper) 0%, var(--paper) 44%, var(--mist) 58%, var(--blush) 100%);
    box-shadow: 0 6px 24px rgba(0,0,0,.12);
    overflow: hidden;
    display: flex; flex-direction: column;
  }
  .sheet-body {
    flex: 1;
    display: grid;
    grid-template-columns: 1fr 1fr;
    gap: 0 18px;
    padding: 0 22px 0 0;
    position: relative;
  }
  .column { padding-top: 14px; display: flex; flex-direction: column; gap: 7px; }
  .column-left { padding-left: 22px; padding-top: 0; }
  .masthead {
    margin-left: -22px;
    margin-right: -40px;
    padding: 26px 22px 14px 40px;
    background: linear-gradient(100deg, var(--red) 0%, var(--red-soft) 55%, rgba(240,147,149,.5) 85%, rgba(248,211,212,0) 100%);
    color: var(--paper);
    margin-bottom: 4px;
  }
  .masthead-kicker { font-family: "Merriweather", Georgia, serif; font-weight: 700; font-size: 17px; line-height: 1.15; }
  .masthead-title { font-family: "Merriweather", Georgia, serif; font-weight: 900; font-size: 40px; line-height: 1; letter-spacing: 1px; }
  .faq-item { display: grid; grid-template-columns: 16px 1fr; gap: 0 8px; }
  .faq-number {
    width: 14px; height: 14px; border-radius: 50%;
    background: var(--red); color: var(--paper);
    font-family: "Merriweather", Georgia, serif; font-weight: 700; font-size: 7.5px;
    display: flex; align-items: center; justify-content: center;
    margin-top: 1px;
  }
  .faq-question { font-weight: 700; color: var(--red); font-size: 7.2px; line-height: 1.25; margin-bottom: 2px; }
  .faq-answer { font-size: 6.6px; line-height: 1.3; color: var(--ink-soft); }
  .faq-answer ul { padding-left: 10px; margin-top: 2px; }
  .sheet-footer {
    height: 46px;
    background: var(--paper);
    display: flex; align-items: center;
    padding: 0 24px 0 28px; gap: 18px;
    font-size: 8px; color: var(--ink);
  }
  .contact { display: flex; align-items: center; gap: 5px; }
  .contact svg { width: 10px; height: 10px; fill: var(--ink); }
  .brand { margin-left: auto; display: flex; align-items: center; gap: 8px; }
  .brand-name { font-family: "Merriweather", Georgia, serif; font-weight: 900; font-size: 11px; color: var(--red); }
  .brand-unit { font-family: "Merriweather", Georgia, serif; font-weight: 700; font-size: 7px; line-height: 1.2; text-transform: uppercase; letter-spacing: .5px; border-left: 1px solid var(--ink); padding-left: 8px; }
</style>
</head>
<body>
<main class="sheet">
  <div class="sheet-body">
    <section class="column column-left">
      <header class="masthead">
        <p class="masthead-kicker">In-Aisle Customer<br>Special Orders</p>
        <h1 class="masthead-title">FAQ</h1>
      </header>

      <article class="faq-item">
        <span class="faq-number">1</span>
        <div>
          <h2 class="faq-question">Why should I care about this new Customer Special Order Process?</h2>
          <p class="faq-answer">Based on a recent study, the average ticket of a customer special order is more than three times bigger than that of a regular transaction. In the same video, shoppers are increasingly expecting retailers to offer what they want, when they want it. With the new process, the special order process is now much more streamlined, pairing BirchNet, the retailer mobile app and the point of sale for quicker, tidier order handling.</p>
        </div>
      </article>

      <article class="faq-item">
        <span class="faq-number">2</span>
        <div>
          <h2 class="faq-question">We do mobile special orders, but there are times in the process it is more convenient to use a computer terminal versus mobile. Has there been any changes?</h2>
          <p class="faq-answer">One of the biggest developments rolled out in BirchNet is the ability to enter all customer information pertaining to a special order. Specifically, leveraging BirchNet, customer orders can be processed at a stand terminal or counter during a quiet moment, bringing the information into your register and keeping the record tidy.</p>
        </div>
      </article>

      <article class="faq-item">
        <span class="faq-number">3</span>
        <div>
          <h2 class="faq-question">Super important to the special orders is communicating back to the customer the status of their order. How is this accomplished?</h2>
          <p class="faq-answer">During the order entry process, the sales associate obtains a phone number from the customer so that they receive notifications. In turn, customers receive a text when their order is acknowledged, when the order is ready for pick up, or the date of home delivery.</p>
        </div>
      </article>

      <article class="faq-item">
        <span class="faq-number">4</span>
        <div>
          <h2 class="faq-question">I hear different things. When is the right time to invoice the special order?</h2>
          <p class="faq-answer">Under the enhanced special order process, invoice them immediately after receipt from the warehouse. Upon completion, sales are recorded to the register, and all guaranteed quantities are released.</p>
        </div>
      </article>

      <article class="faq-item">
        <span class="faq-number">5</span>
        <div>
          <h2 class="faq-question">Three times or more, customers call to ask about the status of their special orders. Which tool should I use to check progress?</h2>
          <p class="faq-answer">Yes. Moving forward, in these instances, from the dashboard in the Retailer Mobile App Customer Order Status screen, you are able to look up the status of the order by customer name, order number or phone. All order data is now captured in these programs.</p>
        </div>
      </article>
    </section>

    <section class="column column-right">
      <article class="faq-item">
        <span class="faq-number">6</span>
        <div>
          <h2 class="faq-question">I see the value in the process, but I would like more understanding to implement. Where do I go?</h2>
          <p class="faq-answer">Birchpoint Supply recently posted an online resource page for a step-by-step understanding and short training on best practices. Path: BirchNet &gt; Store Ops &gt; Special Orders.</p>
        </div>
      </article>

      <article class="faq-item">
        <span class="faq-number">7</span>
        <div>
          <h2 class="faq-question">I reviewed the best practice on deposits. Why do I need to take a 100% deposit?</h2>
          <p class="faq-answer">Studies show that 25% of customer special orders are never picked up by the customer, resulting in a potential lost profit. Taking a full deposit eliminates the financial risk on the part of the store, and helps create urgency for the customer to pick up the product.</p>
        </div>
      </article>

      <article class="faq-item">
        <span class="faq-number">8</span>
        <div>
          <h2 class="faq-question">What are some important but underutilized best practices I should be doing with every special order I process?</h2>
          <div class="faq-answer">Though the Birchpoint Supply Customer Special Orders (in-aisle) document outlines each best practice, some of the top ones include:
            <ul>
              <li>Inform customers of your policy to have orders picked up within five days of notification.</li>
              <li>Sell the item in the order multiple in which it comes in, particularly if you don't stock the product.</li>
              <li>For a clean process, do not include any items to be taken by the customer that day on the same transaction.</li>
            </ul>
          </div>
        </div>
      </article>

      <article class="faq-item">
        <span class="faq-number">9</span>
        <div>
          <h2 class="faq-question">I have a whole bunch of special orders from mobile that have not been received in the retailer mobile app. How do I get rid of them to start with a clean slate?</h2>
          <p class="faq-answer">Old orders already received by the customer can be removed through BirchNet Delivery and Services App or through Order Tracking. Doing so deletes them from the Retailer Mobile App without notification going to the customer.</p>
        </div>
      </article>

      <article class="faq-item">
        <span class="faq-number">10</span>
        <div>
          <h2 class="faq-question">Are my in-aisle customer special orders required to be linked to a Birchpoint Rewards account?</h2>
          <p class="faq-answer">Birchpoint currently only tracks a customer's related orders. In-aisle customer special orders can be received via BirchNet's order tracking system and the retailer mobile app order lookup feature.</p>
        </div>
      </article>

      <article class="faq-item">
        <span class="faq-number">11</span>
        <div>
          <h2 class="faq-question">What cost is posted to the ledger when the order is sent to the warehouse?</h2>
          <p class="faq-answer">Right now BirchNet's pricing based on your pricing level. You may notice a small difference between retail when entering the order and the posted price. The other exception relates to items where there is variation in the unit of measure on the order.</p>
        </div>
      </article>
    </section>
  </div>

  <footer class="sheet-footer">
    <span class="contact">
      <svg viewBox="0 0 24 24" aria-hidden="true"><path d="M6.6 10.8a15.1 15.1 0 0 0 6.6 6.6l2.2-2.2c.3-.3.7-.4 1-.2 1.1.4 2.3.6 3.6.6.6 0 1 .4 1 1V20c0 .6-.4 1-1 1A17 17 0 0 1 3 4c0-.6.4-1 1-1h3.5c.6 0 1 .4 1 1 0 1.3.2 2.5.6 3.6.1.3 0 .7-.2 1z"/></svg>
      1 555.014.2290
    </span>
    <span class="contact">
      <svg viewBox="0 0 24 24" aria-hidden="true"><path d="M2 5h20v14H2zM4 7v.5l8 5 8-5V7l-8 5z"/></svg>
      storeops@birchpointsupply.com
    </span>
    <div class="brand">
      <span class="brand-name">Birchpoint Supply</span>
      <span class="brand-unit">Store Systems &amp;<br>Operations</span>
    </div>
  </footer>
</main>
</body>
</html>
```